Contact card for an aggressive entrepreneur

I am looking for a business/contact card as an individual. I operate under the company name The Varlow Circle, LLC (but don't generally use that other than for billing). I have explored a few ideas and am now turning to makerhive to connect with people more creative than me. I am trying to capture a diverse set of passions, which I will summarize with the following keywords (which may or may not be ON the card and are in no particular order):

entrepreneur
shark diver
MBA
visionary
defenseman
marketing guru
hockey coach
teacher
reader
writer
cook
captain
scuba diver
beach bum
Type A
Coach
Leader
Captain
Founder
founder
leader
focused
driven
teammate father

hope that makes some sense!
Updates

Please note the photo is for reference - unless there is a really creative way to use it I do not need a card with a head shot (I am not a model or an actor!)

Project Deadline Extended
Reason: There have been several requests to submit designs so we will close this project this Wednesday and select a design by this Friday. Thank you to all for your great ideas and submissions!

I am reviewing the designs and will select one by end of day tomorrow, Tuesday, EST
Thank you to all who participated!

Target Market(s)

everyone from business contacts to personal acquaintances

Industry/Entity Type

Business

Requirements
Must have
• Must be utterly original, extraordinary and memorable.
How it achieves that is up to you!
Essential contact information that needs to be included:

phone: (917) 555-4173
email: tomas@varlowcircle.example
skype: tomas.varlow
Nice to have
• A striking visual whether that is a photo or illustration
Some way of conveying the diversity of what I am and what I do
Feel free to use the printing or physical material of the card to make it stand out.
Should not have
• I am not into "logos" but that being said I do not want to limit creativity in any way so feel free to ignore any part of this brief if you disagree with me. No need to use the attached photo of me, but that's what I look like.

```html
<!DOCTYPE html>
<html lang="en">
<head>
<meta charset="utf-8">
<title>Tomas Varlow — Contact Card</title>
<link href="https://fonts.googleapis.com/css2?family=Arimo:wght@400;700&display=swap" rel="stylesheet">
<style>
  :root {
    --card-bg: #000000;
    --word-tone: #5b5b5b;
    --word-tone-side: #4a4a4a;
    --word-echo: #2e2e2e;
    --name-tone: #ffffff;
    --contact-tone: #ffffff;
  }
  html, body {
    margin: 0;
    padding: 0;
    width: 1200px;
    height: 686px;
    overflow: hidden;
    background: var(--card-bg);
  }
  .card {
    display: block;
    width: 1200px;
    height: 686px;
    font-family: "Arimo", Arial, sans-serif;
  }
  .keywords text { fill: var(--word-tone); font-weight: 400; }
  .keywords .keyword-bold { font-weight: 700; }
  .keywords .keyword-side { fill: var(--word-tone-side); }
  .keywords-low text { fill: var(--word-echo); font-weight: 400; }
  .keywords-low .keyword-bold { font-weight: 700; }
  .holder-name {
    font-size: 68px;
    font-weight: 400;
  }
  .contact-line {
    fill: var(--contact-tone);
    font-size: 44px;
  }
</style>
</head>
<body>
<svg class="card" viewBox="0 0 1050 600" preserveAspectRatio="none" xmlns="http://www.w3.org/2000/svg" aria-label="Contact card for Tomas Varlow">
  <defs>
    <filter id="name-glow" x="-5%" y="-20%" width="110%" height="140%">
      <feDropShadow dx="0" dy="2" stdDeviation="1.5" flood-color="#777" flood-opacity="0.6"/>
    </filter>
    <linearGradient id="name-shade" x1="0" y1="0" x2="0" y2="1">
      <stop offset="0" stop-color="#ffffff"/>
      <stop offset="1" stop-color="#d6d6d6"/>
    </linearGradient>
  </defs>

  <rect class="card-ground" width="1050" height="600" fill="var(--card-bg)"/>

  <g class="keywords">
    <text x="25" y="57" font-size="42" textLength="230" lengthAdjust="spacing">CAPTAIN</text>
    <text x="70" y="107" font-size="42" textLength="205" lengthAdjust="spacing">LEADER</text>
    <text x="70" y="155" font-size="42" textLength="180" lengthAdjust="spacing">COACH</text>
    <text class="keyword-side" transform="translate(25,75) rotate(90)" font-size="42" textLength="255" lengthAdjust="spacing">FOUNDER</text>
    <text class="keyword-bold" x="300" y="125" font-size="47" textLength="400" lengthAdjust="spacing">STRATEGIST</text>
    <text x="300" y="172" font-size="34" textLength="160" lengthAdjust="spacing">WRITER</text>
    <text x="490" y="187" font-size="34" textLength="165" lengthAdjust="spacing">READER</text>
    <text x="714" y="90" font-size="38" textLength="222" lengthAdjust="spacing">TEACHER</text>
    <text class="keyword-bold" x="740" y="173" font-size="50" textLength="250" lengthAdjust="spacing">DRIVEN</text>
  </g>

  <g class="keywords-low" transform="rotate(180 525 300)" aria-hidden="true">
    <text x="25" y="57" font-size="42" textLength="215" lengthAdjust="spacing">MENTOR</text>
    <text x="70" y="107" font-size="42" textLength="270" lengthAdjust="spacing">BEACH BUM</text>
    <text x="70" y="155" font-size="42" textLength="190" lengthAdjust="spacing">TYPE A</text>
    <text transform="translate(25,75) rotate(90)" font-size="42" textLength="210" lengthAdjust="spacing">FATHER</text>
    <text class="keyword-bold" x="400" y="128" font-size="47" textLength="360" lengthAdjust="spacing">MARKETER</text>
    <text x="520" y="178" font-size="34" textLength="120" lengthAdjust="spacing">COOK</text>
    <text class="keyword-bold" x="720" y="168" font-size="48" textLength="260" lengthAdjust="spacing">DEFENSE</text>
  </g>

  <text class="holder-name" x="130" y="307" textLength="805" lengthAdjust="spacing" fill="url(#name-shade)" filter="url(#name-glow)">TOMAS VARLOW</text>

  <g class="contact-block">
    <text class="contact-line" x="25" y="388" textLength="587" lengthAdjust="spacing">phone: (917) 555-4173</text>
    <text class="contact-line" x="25" y="472" textLength="795" lengthAdjust="spacingAndGlyphs">email: tomas@varlowcircle.example</text>
    <text class="contact-line" x="25" y="555" textLength="483" lengthAdjust="spacing">skype: tomas.varlow</text>
  </g>
</svg>
</body>
</html>
```